TBM Behaviours

As per attached we have a "Our Purpose" Ribbon and "Behaviors Supporting our Pursuit" slide Sketch Bazaar designed the logo for the Tarwin Bluff Vision (Project ID 5081634 ), it would be good to get this built in professionally rather than just cut in as per attached. Like wise with the Tarwin Bluff Mission.

Each Behavior would be as per design, with them Grouped as pictured, but also individual on separate slides, both with words and without allowing us to used them in many different formats.

From there some creativity to help us promote and deploy these to our business.

Target Market(s)

This is for our workforce

Requirements
Must have
• Include Our Purpose and The behaviors.

```html
<!DOCTYPE html>
<html lang="en">
<head>
<meta charset="utf-8">
<title>TBM Behaviours</title>
<link rel="stylesheet" href="https://fonts.googleapis.com/css2?family=Montserrat:wght@300;400;600;700&display=swap">
<style>
:root{
  --board:#cbcbcb;
  --paper:#ffffff;
  --ink:#2b2b2b;
  --dark:#332c2a;
  --blue:#13627d;
  --yellow:#f9bf15;
  --slate:#57768a;
  --orange:#e35727;
  --teal:#048a80;
  --green:#b5d56b;
  --brand:#1d4f9c;
}
html,body{margin:0;padding:0;overflow:hidden}
body{width:1200px;height:1167px;background:var(--board);position:relative;font-family:"Montserrat",Arial,sans-serif}
.slide{position:absolute;display:block;background:var(--paper);box-shadow:0 6px 6px -4px rgba(0,0,0,.25)}
.slide-purpose-lg{left:677px;top:36px;width:296px;height:236px}
.slide-purpose-sm{left:166px;top:343px;width:181px;height:145px}
.slide-sm{width:181px;height:145px}
.slide-lg{width:297px;height:237px}
.col-sm-1{left:80px}.col-sm-2{left:273px}
.row-sm-1{top:511px}.row-sm-2{top:688px}.row-sm-3{top:861px}
.col-lg-1{left:535px}.col-lg-2{left:851px}
.row-lg-1{top:311px}.row-lg-2{top:602px}.row-lg-3{top:886px}
.t-bold{font-weight:700}
.t-light{font-weight:300}
.title{fill:#fff;font-size:17px;text-anchor:middle}
.desc{fill:var(--ink);font-size:6.6px;text-anchor:middle}
.icon{fill:none;stroke:#fff;stroke-width:3;stroke-linecap:round;stroke-linejoin:round}
.brand-name{fill:var(--brand);font-size:12px;font-weight:700;text-anchor:middle}
.p-head{fill:#fff;font-size:5.8px;font-weight:600}
.p-body{fill:#fff;font-size:4.8px;font-weight:600}
.p-label{fill:#fff;font-size:11px;font-weight:600;text-anchor:middle}
.p-desc{fill:var(--ink);font-size:4.6px}
.tile-label{fill:#fff;font-size:3.4px;font-weight:600;text-anchor:middle}
</style>
</head>
<body>

<svg width="0" height="0" style="position:absolute" aria-hidden="true">
  <defs>
    <!-- icons, drawn in a -40..40 box -->
    <symbol id="i-enjoy" viewBox="-40 -40 80 80">
      <g class="icon">
        <path d="M-30 -22l2 -4 2 4M-12 -30l2 -4 2 4M8 -30l2 -4 2 4M26 -22l2 -4 2 4"/>
        <path d="M-14 -14q4 -8 10 -6M14 -14q-4 -8 -10 -6"/>
        <circle cx="-18" cy="0" r="4"/><circle cx="0" cy="-2" r="4"/><circle cx="18" cy="0" r="4"/>
        <path d="M-30 4l8 6h8l8 -6M-24 10v20M-12 10v20M-6 6h12M-6 8v22M6 8v22M6 4l8 6h8l8 -6M12 10v20M24 10v20"/>
      </g>
    </symbol>
    <symbol id="i-quality" viewBox="-40 -40 80 80">
      <g class="icon">
        <path d="M-30 -20v-10h10M20 -30h10v10M30 20v10h-10M-20 30h-10v-10"/>
        <path d="M0 -38v8M0 30v8M-38 0h8M30 0h8"/>
        <circle cx="0" cy="-4" r="14"/>
        <path d="M-6 -4l4 5 9 -9"/>
        <path d="M-8 8l-5 14 6 -2 4 5 3 -14M8 8l5 14 -6 -2 -4 5 -3 -14"/>
      </g>
    </symbol>
    <symbol id="i-caring" viewBox="-40 -40 80 80">
      <g class="icon">
        <path d="M-8 -18q10 -12 26 -16v16q-10 6 -20 4l-8 8"/>
        <path d="M0 8c-6 -6 -12 -8 -12 -14a6 6 0 0 1 12 -2a6 6 0 0 1 12 2c0 6 -6 8 -12 14z"/>
        <path d="M-30 14h14l12 6h14q6 0 6 -5l6 -3q6 0 -2 8l-12 10h-24l-14 -6z"/>
      </g>
    </symbol>
    <symbol id="i-diversity" viewBox="-40 -40 80 80">
      <g class="icon">
        <rect x="-24" y="-34" width="16" height="34" rx="5"/>
        <rect x="0" y="-24" width="34" height="16" rx="5"/>
        <rect x="8" y="0" width="16" height="34" rx="5"/>
        <rect x="-34" y="8" width="34" height="16" rx="5"/>
      </g>
    </symbol>
    <symbol id="i-team" viewBox="-40 -40 80 80">
      <g class="icon">
        <circle cx="-14" cy="-4" r="10"/><circle cx="16" cy="-16" r="10"/><circle cx="6" cy="22" r="10"/>
        <circle cx="-30" cy="-26" r="4"/><circle cx="-32" cy="22" r="4"/><circle cx="34" cy="6" r="4"/><circle cx="-8" cy="-32" r="4"/>
        <path d="M-4 -8l10 -4M-8 4l8 10M14 -6l-4 18M-27 -23l-6 11M-28 19l6 -16M30 4l-6 -12M-8 -28l-3 14"/>
      </g>
    </symbol>
    <symbol id="i-customer" viewBox="-40 -40 80 80">
      <g class="icon">
        <circle cx="0" cy="-10" r="12"/>
        <path d="M-16 -10a16 16 0 0 1 32 0M-16 -12v8M16 -12v8M16 -4q0 10 -10 10h-4"/>
        <path d="M-26 34v-8q0 -10 14 -12l12 10 12 -10q14 2 14 12v8z"/>
        <path d="M-6 16l6 6 6 -6"/>
      </g>
    </symbol>

    <!-- slide furniture -->
    <symbol id="band-gaps" viewBox="0 0 484 387">
      <polygon fill="#fff" points="178,72 190,72 110,274 98,274"/>
      <polygon fill="#fff" points="374,72 386,72 306,274 294,274"/>
    </symbol>
    <symbol id="slide-foot" viewBox="0 0 484 387">
      <polygon fill="var(--orange)" points="0,358 423,358 419,365 0,365"/>
      <text class="brand-name" x="450" y="370">NCA</text>
    </symbol>

    <!-- behaviour headers -->
    <symbol id="b-enjoy" viewBox="0 0 484 387">
      <rect y="72" width="484" height="202" fill="var(--blue)"/>
      <use href="#band-gaps" width="484" height="387"/>
      <text class="title t-bold" x="240" y="125">Enjoy what</text>
      <text class="title t-bold" x="242" y="146">we do</text>
      <use href="#i-enjoy" x="202" y="160" width="80" height="80"/>
      <use href="#slide-foot" width="484" height="387"/>
    </symbol>
    <symbol id="b-quality" viewBox="0 0 484 387">
      <rect y="72" width="484" height="202" fill="var(--yellow)"/>
      <use href="#band-gaps" width="484" height="387"/>
      <text class="title t-light" x="244" y="125" font-size="15">Focus on</text>
      <text class="title t-bold" x="242" y="146">Quality</text>
      <use href="#i-quality" x="202" y="160" width="80" height="80"/>
      <use href="#slide-foot" width="484" height="387"/>
    </symbol>
    <symbol id="b-caring" viewBox="0 0 484 387">
      <rect y="72" width="484" height="202" fill="var(--slate)"/>
      <use href="#band-gaps" width="484" height="387"/>
      <text class="title t-light" x="246" y="129">Caring</text>
      <use href="#i-caring" x="206" y="148" width="80" height="80"/>
      <use href="#slide-foot" width="484" height="387"/>
    </symbol>
    <symbol id="b-diversity" viewBox="0 0 484 387">
      <rect y="72" width="484" height="202" fill="var(--orange)"/>
      <use href="#band-gaps" width="484" height="387"/>
      <text class="title t-light" x="242" y="120" font-size="15">Value</text>
      <text class="title t-bold" x="242" y="140">Diversity</text>
      <use href="#i-diversity" x="204" y="154" width="78" height="78"/>
      <use href="#slide-foot" width="484" height="387"/>
    </symbol>
    <symbol id="b-team" viewBox="0 0 484 387">
      <rect y="72" width="484" height="202" fill="var(--teal)"/>
      <use href="#band-gaps" width="484" height="387"/>
      <text class="title t-bold" x="242" y="118">Team Work</text>
      <use href="#i-team" x="200" y="136" width="84" height="84"/>
      <use href="#slide-foot" width="484" height="387"/>
    </symbol>
    <symbol id="b-customer" viewBox="0 0 484 387">
      <rect y="72" width="484" height="202" fill="var(--green)"/>
      <use href="#band-gaps" width="484" height="387"/>
      <text class="title t-light" x="242" y="124" font-size="15">Serve</text>
      <text class="title t-bold" x="242" y="144">Our Customer</text>
      <use href="#i-customer" x="204" y="156" width="78" height="78"/>
      <use href="#slide-foot" width="484" height="387"/>
    </symbol>

    <!-- purpose slide -->
    <symbol id="purpose" viewBox="0 0 484 387">
      <rect width="484" height="387" fill="#fff"/>
      <polygon fill="var(--dark)" points="196,14 302,14 294,39 188,39"/>
      <text class="p-label" x="245" y="31">Our Purpose</text>

      <polygon fill="var(--dark)" points="51,58 155,58 120,170 16,170"/>
      <polygon fill="var(--orange)" points="158,58 259,58 224,170 122,170"/>
      <polygon fill="var(--dark)" points="262,58 363,58 328,170 226,170"/>
      <polygon fill="var(--orange)" points="366,58 467,58 432,170 330,170"/>

      <text class="p-head" x="60" y="70">Korvan's Purpose</text>
      <text class="p-body" x="68" y="103"><tspan x="68">To Bring People</tspan><tspan x="68" dy="6">and Resources</tspan><tspan x="68" dy="6">Together to Build a</tspan><tspan x="68" dy="6">Better World</tspan></text>
      <text x="30" y="164" fill="var(--orange)" font-size="12" font-weight="700">KORVAN</text>

      <text class="p-head" x="166" y="70">Tarwin Bluff Vision</text>
      <text x="190" y="120" fill="#fff" font-size="9" font-weight="700" text-anchor="middle">TARWIN BLUFF</text>
      <text class="p-body" x="138" y="150"><tspan x="138">Vision aligns you with goals</tspan><tspan x="138" dy="6">and the destination you are</tspan><tspan x="138" dy="6">moving towards</tspan></text>

      <text class="p-head" x="270" y="70">Tarwin Bluff Mission</text>
      <rect x="266" y="103" width="9" height="9" fill="var(--orange)"/>
      <text x="279" y="111" fill="var(--orange)" font-size="9" font-weight="700">ONECREW</text>
      <text class="p-body" x="246" y="150"><tspan x="246">Mission empowers you with</tspan><tspan x="246" dy="6">actions to accomplish your</tspan><tspan x="246" dy="6">vision</tspan></text>

      <text class="p-head" x="372" y="70"><tspan x="372">Tarwin Bluff Coal Mine</tspan><tspan x="372" dy="7">Worker</tspan></text>
      <text class="p-body" x="366" y="116">I come to Tarwin Bluff to........</text>
      <rect x="374" y="140" width="40" height="20" fill="#fff"/>
      <text x="394" y="153" fill="var(--brand)" font-size="8" font-weight="700" text-anchor="middle">NCA</text>

      <polygon fill="var(--orange)" points="110,200 383,200 376,224 103,224"/>
      <text class="p-label" x="243" y="216">Behaviours Supporting our Pursuit</text>

      <g>
        <polygon fill="var(--blue)" points="44,237 84,237 66,282 26,282"/>
        <text class="tile-label" x="56" y="247">Enjoy what we do</text>
        <use href="#i-enjoy" x="45" y="253" width="22" height="22"/>
        <text class="p-desc" x="88" y="251"><tspan x="88">We all create a fun and</tspan><tspan x="88" dy="5.5">enjoyable work environment that</tspan><tspan x="88" dy="5.5">people are <tspan font-weight="700">proud</tspan> of</tspan></text>

        <polygon fill="var(--yellow)" points="194,237 234,237 216,282 176,282"/>
        <text class="tile-label" x="206" y="247">Focus on Quality</text>
        <use href="#i-quality" x="195" y="253" width="22" height="22"/>
        <text class="p-desc" x="238" y="251"><tspan x="238">Everyone strives for <tspan font-weight="700">quality</tspan></tspan><tspan x="238" dy="5.5">outcomes by removing waste,</tspan><tspan x="238" dy="5.5">rework and frustration</tspan></text>

        <polygon fill="var(--slate)" points="342,237 382,237 364,282 324,282"/>
        <text class="tile-label" x="354" y="247">Caring</text>
        <use href="#i-caring" x="343" y="253" width="22" height="22"/>
        <text class="p-desc" x="384" y="244"><tspan x="384">We are genuinely interested</tspan><tspan x="384" dy="5.5">in the safety and wellbeing of</tspan><tspan x="384" dy="5.5">all our people, we respect</tspan><tspan x="384" dy="5.5">each other and always feel</tspan><tspan x="384" dy="5.5">safe to speak up</tspan></text>
      </g>
      <g>
        <polygon fill="var(--orange)" points="44,309 84,309 66,354 26,354"/>
        <text class="tile-label" x="56" y="319">Value Diversity</text>
        <use href="#i-diversity" x="45" y="325" width="22" height="22"/>
        <text class="p-desc" x="88" y="319"><tspan x="88">We <tspan font-weight="700">value</tspan> different backgrounds</tspan><tspan x="88" dy="5.5">and experience, enabling our</tspan><tspan x="88" dy="5.5">teams success. We promote an</tspan><tspan x="88" dy="5.5">environment where you can be</tspan><tspan x="88" dy="5.5">100% yourself</tspan></text>

        <polygon fill="var(--teal)" points="194,309 234,309 216,354 176,354"/>
        <text class="tile-label" x="206" y="319">Team Work</text>
        <use href="#i-team" x="195" y="325" width="22" height="22"/>
        <text class="p-desc" x="238" y="314"><tspan x="238">Making tomorrow better than</tspan><tspan x="238" dy="5.5">today by continuously</tspan><tspan x="238" dy="5.5">improving, working as <tspan font-weight="700">OneCrew</tspan>,</tspan><tspan x="238" dy="5.5">sharing, leveraging our</tspan><tspan x="238" dy="5.5">strengths and celebrating our</tspan><tspan x="238" dy="5.5">successes</tspan></text>

        <polygon fill="var(--green)" points="342,309 382,309 364,354 324,354"/>
        <text class="tile-label" x="354" y="319">Serve Our Customer</text>
        <use href="#i-customer" x="343" y="325" width="22" height="22"/>
        <text class="p-desc" x="384" y="322"><tspan x="384">We know who our customers</tspan><tspan x="384" dy="5.5">are and regularly check on</tspan><tspan x="384" dy="5.5">how we are delivering to</tspan><tspan x="384" dy="5.5">their needs</tspan></text>
      </g>
    </symbol>
  </defs>
</svg>

<!-- Our Purpose slides -->
<svg class="slide slide-purpose-lg" viewBox="0 0 484 387"><use href="#purpose" width="484" height="387"/></svg>
<svg class="slide slide-purpose-sm" viewBox="0 0 484 387"><use href="#purpose" width="484" height="387"/></svg>

<!-- Behaviour slides without words -->
<svg class="slide slide-sm col-sm-1 row-sm-1" viewBox="0 0 484 387"><use href="#b-enjoy" width="484" height="387"/></svg>
<svg class="slide slide-sm col-sm-2 row-sm-1" viewBox="0 0 484 387"><use href="#b-quality" width="484" height="387"/></svg>
<svg class="slide slide-sm col-sm-1 row-sm-2" viewBox="0 0 484 387"><use href="#b-caring" width="484" height="387"/></svg>
<svg class="slide slide-sm col-sm-2 row-sm-2" viewBox="0 0 484 387"><use href="#b-diversity" width="484" height="387"/></svg>
<svg class="slide slide-sm col-sm-1 row-sm-3" viewBox="0 0 484 387"><use href="#b-team" width="484" height="387"/></svg>
<svg class="slide slide-sm col-sm-2 row-sm-3" viewBox="0 0 484 387"><use href="#b-customer" width="484" height="387"/></svg>

<!-- Behaviour slides with words -->
<svg class="slide slide-lg col-lg-1 row-lg-1" viewBox="0 0 484 387">
  <use href="#b-enjoy" width="484" height="387"/>
  <text class="desc" x="242" y="310"><tspan x="242">We all create a fun and</tspan><tspan x="242" dy="8">enjoyable work environment that people are</tspan><tspan x="242" dy="8" font-weight="700">proud <tspan font-weight="400">of</tspan></tspan></text>
</svg>
<svg class="slide slide-lg col-lg-2 row-lg-1" viewBox="0 0 484 387">
  <use href="#b-quality" width="484" height="387"/>
  <text class="desc" x="242" y="318"><tspan x="242">Everyone strives for <tspan font-weight="700">quality</tspan> outcomes</tspan><tspan x="242" dy="8">by removing waste, rework and frustration</tspan></text>
</svg>
<svg class="slide slide-lg col-lg-1 row-lg-2" viewBox="0 0 484 387">
  <use href="#b-caring" width="484" height="387"/>
  <text class="desc" x="242" y="306"><tspan x="242">We are genuinely interested in the safety and</tspan><tspan x="242" dy="8">wellbeing of all our people, we respect each</tspan><tspan x="242" dy="8">other and always feel safe to speak up</tspan></text>
</svg>
<svg class="slide slide-lg col-lg-2 row-lg-2" viewBox="0 0 484 387">
  <use href="#b-diversity" width="484" height="387"/>
  <text class="desc" x="242" y="306"><tspan x="242">We <tspan font-weight="700">value</tspan> different backgrounds and experience,</tspan><tspan x="242" dy="8">enabling our teams success. We promote an</tspan><tspan x="242" dy="8">environment where you can be 100% yourself</tspan></text>
</svg>
<svg class="slide slide-lg col-lg-1 row-lg-3" viewBox="0 0 484 387">
  <use href="#b-team" width="484" height="387"/>
  <text class="desc" x="242" y="306"><tspan x="242">Making tomorrow better than today by continuously</tspan><tspan x="242" dy="8">improving, working as <tspan font-weight="700">OneCrew</tspan>, sharing, leveraging our</tspan><tspan x="242" dy="8">strengths and celebrating our successes</tspan></text>
</svg>
<svg class="slide slide-lg col-lg-2 row-lg-3" viewBox="0 0 484 387">
  <use href="#b-customer" width="484" height="387"/>
  <text class="desc" x="242" y="312"><tspan x="242">We know who our customers are and regularly</tspan><tspan x="242" dy="8">check on how we are delivering to their needs</tspan></text>
</svg>

</body>
</html>
```